nonprofit organization looking for sleek new design

We need a fresh new look for this nonprofit organization, Harbor Aid For Outreach Groups, INC (HAFOG, Inc.). This organization provides educational, nutritional, dental health, and specialized services to Tall Meadow children, aiming to support families meeting federal income poverty guidelines. Our mission is clear: "Creating a brighter future for the children and la familia." We focus on child development, family wellness, staff growth, and community partnerships.

```html
<!DOCTYPE html>
<html lang="en">
<head>
<meta charset="utf-8">
<title>HAFOG, Inc. — Creating a brighter future</title>
<link href="https://fonts.googleapis.com/css2?family=Poppins:wght@300;400;500;600;700;800&display=swap" rel="stylesheet">
<style>
:root{
  --red:#e31b2f;
  --blue:#1565b8;
  --blue-dark:#0f57a6;
  --ink:#222;
  --muted:#555;
  --light:#e9eff8;
  --footer:#111;
  --white:#fff;
}
*{box-sizing:border-box;margin:0;padding:0}
html,body{width:1200px;height:4699px;overflow:hidden}
body{font-family:'Poppins',sans-serif;color:var(--ink);background:var(--white);position:relative}
.abs{position:absolute}
.btn{position:absolute;display:flex;align-items:center;justify-content:center;gap:12px;color:#fff;font-weight:600;font-size:16px;border-radius:3px}
.btn .arr{width:20px;height:20px;border-radius:50%;background:#fff;display:inline-flex;align-items:center;justify-content:center}
.btn.red{background:var(--red)}
.btn.blue{background:var(--blue)}
.btn.dark{background:#111}
.section-title{position:absolute;left:0;width:1200px;text-align:center;font-size:38px;font-weight:400}
.section-title b{font-weight:700}
.rule{position:absolute;height:4px;width:38px;background:var(--red)}

/* nav */
.nav{position:absolute;top:0;left:0;width:1200px;height:88px;z-index:3;border-bottom:1px solid rgba(21,101,184,.25);background:rgba(255,255,255,.55)}
.brand{position:absolute;left:110px;top:6px;display:flex;align-items:center;gap:10px;font-weight:700;font-size:20px;color:var(--ink)}
.brand i{width:22px;height:22px;border-radius:50%;background:var(--red);display:block}
.menu{position:absolute;left:458px;top:30px;display:flex;gap:44px;font-size:16px}
.menu .on{color:var(--red)}

/* hero */
.hero{position:absolute;top:0;left:0;width:1200px;height:712px;background:linear-gradient(180deg,#f2f2f2 0%,#e6e4e2 55%,#d9d5d0 100%)}
.hero-photo{position:absolute;left:0;top:330px;width:1200px;height:382px;background:linear-gradient(180deg,#d8d3ce,#cfc8c2);}
.hero h1{position:absolute;top:120px;left:0;width:1200px;text-align:center;font-size:55px;font-weight:800;line-height:60px;color:#2c2c2c}
.hero h1 span{color:var(--blue)}
.dots{position:absolute;display:flex;gap:8px}
.dots i{width:12px;height:12px;border-radius:50%;border:1.5px solid #777;display:block}
.dots i.on{background:var(--red);border-color:var(--red)}

/* about */
.about-photo{position:absolute;left:120px;top:802px;width:420px;height:420px;border-radius:50%;border:8px solid var(--blue);background:radial-gradient(circle at 50% 45%,#e0b99a,#8a6a55 60%,#4d4036)}
.about h2{position:absolute;left:600px;top:790px;font-size:38px;font-weight:400}
.about h2 b{font-weight:700}
.about p{position:absolute;left:600px;width:472px;font-size:14px;line-height:25px;color:var(--muted);text-align:justify}

/* services */
.services{position:absolute;top:1313px;left:0;width:1200px;height:808px;background:var(--blue-dark)}
.card{position:absolute;width:236px;background:#fff;border-radius:6px;overflow:hidden;text-align:center;box-shadow:0 4px 14px rgba(0,0,0,.2)}
.card .img{height:222px}
.card h3{font-size:18px;font-weight:500;margin:20px 0 10px}
.card p{font-size:12.5px;line-height:19px;color:var(--muted);padding:0 14px}
.card a{display:inline-block;font-size:12px;margin:12px 0 20px;border-bottom:1px solid #333;color:var(--ink)}

/* focus */
.focus-label{position:absolute;font-size:19px;line-height:24px}
.focus-icon{position:absolute;width:80px;height:80px;border-radius:50%;background:#fff;box-shadow:0 2px 8px rgba(0,0,0,.15);display:flex;align-items:center;justify-content:center}

/* testimonials */
.testi-bg{position:absolute;top:2754px;left:0;width:1200px;height:660px;background:var(--light)}
.tcard{position:absolute;top:2920px;width:299px;height:360px;background:#fff;box-shadow:0 3px 12px rgba(0,0,0,.1);padding:26px 14px}
.tcard .q{font-size:60px;font-weight:700;color:var(--red);line-height:44px;letter-spacing:-4px}
.tcard .av{position:absolute;right:28px;top:26px;width:44px;height:44px;border-radius:50%;background:linear-gradient(#cfd8e2,#8fa3b7)}
.tcard h4{font-size:15px;font-weight:600;letter-spacing:1.5px;margin:16px 0 8px}
.tcard p{font-size:14px;line-height:29px;color:#333}
.stars{margin-top:8px;display:flex;gap:2px}

/* contact */
.contact h2{position:absolute;left:146px;top:3512px;font-size:40px;font-weight:400}
.contact h2 b{font-weight:700}
.field{position:absolute;left:627px;width:413px;background:#2a2a2a;color:#ddd;font-size:13px;padding:10px 18px;border-radius:2px}
.info{position:absolute;left:146px;display:flex;gap:20px;align-items:flex-start}
.info .ic{width:36px;height:36px;border-radius:50%;background:var(--red);display:flex;align-items:center;justify-content:center}
.info small{display:block;font-size:12px;color:#666}
.info span{font-size:15px}

/* cta */
.cta{position:absolute;top:3963px;width:482px;height:237px;border-radius:8px;color:#fff;text-align:center;box-shadow:0 6px 14px rgba(0,0,0,.2)}
.cta h3{font-size:24px;font-weight:500;margin-top:80px}

/* footer */
.footer{position:absolute;top:4286px;left:0;width:1200px;height:413px;background:var(--footer);color:#fff}
.fcol{position:absolute;top:68px;font-size:13px;line-height:26px}
.fcol h5{font-size:16px;font-weight:600;margin-bottom:4px}
.fcol .rl{width:52px;height:2px;background:var(--red);margin-bottom:14px}
</style>
</head>
<body>

<section class="hero">
  <div class="hero-photo" role="img" aria-label="Photo of five smiling children sitting together on a carpet"></div>
  <h1>Creating a <span>brighter future</span> for the<br>children and la familia</h1>
  <div class="btn blue" style="left:412px;top:258px;width:154px;height:50px;font-size:15px">Get Started <span class="arr"><svg width="10" height="10" viewBox="0 0 10 10"><path d="M3 1l4 4-4 4" stroke="#1565b8" stroke-width="2" fill="none"/></svg></span></div>
  <div class="btn red" style="left:583px;top:258px;width:206px;height:50px;font-size:15px">Apply for Services <span class="arr"><svg width="10" height="10" viewBox="0 0 10 10"><path d="M3 1l4 4-4 4" stroke="#e31b2f" stroke-width="2" fill="none"/></svg></span></div>
  <div class="dots" style="left:561px;top:685px"><i></i><i class="on"></i><i></i><i></i></div>
</section>

<header class="nav">
  <div class="brand" style="top:30px"><i></i>HAFOG, Inc.</div>
  <nav class="menu"><span class="on">Home</span><span>About</span><span>Services</span><span>Blog</span><span>Testimonials</span></nav>
  <div class="btn red" style="left:992px;top:17px;width:154px;height:50px">Contact Us <span class="arr"><svg width="10" height="10" viewBox="0 0 10 10"><path d="M3 1l4 4-4 4" stroke="#e31b2f" stroke-width="2" fill="none"/></svg></span></div>
</header>

<section class="about">
  <div class="about-photo" role="img" aria-label="Photo of a smiling girl in a classroom with classmates"></div>
  <h2>About <b>Us</b></h2>
  <div class="rule" style="left:600px;top:846px"></div>
  <p style="top:872px">Saerspiciatis undeasepoiise omnis iste natus error sit voluptatem accusan tium doloremque laudantium, totam rem aperiam, ease aque ipsefdsa quae ab illo inventore veritatis ease quasi architecto beatae vitae dicta sunt explicabo. Nemo enim ipsam voluptatem quia volupta sde sessitasese aspernatur autodit aut fugitsdsed quia consequuntur magni dolores eos qui ratione voluptatem sequi nesciunt.</p>
  <p style="top:1061px">Dseste natus error sit voluptatem accusan tium doloremque laudantium, totam rem aperiam, ease aque ipsefdsa quae ab illo inventore veritatis ease quasi architecto.</p>
  <div class="btn red" style="left:600px;top:1158px;width:153px;height:48px">Learn More <span class="arr"><svg width="10" height="10" viewBox="0 0 10 10"><path d="M3 1l4 4-4 4" stroke="#e31b2f" stroke-width="2" fill="none"/></svg></span></div>
</section>

<section class="services">
  <h2 class="section-title" style="top:72px;color:#fff">Our <b>Services</b></h2>
  <div class="rule" style="left:581px;top:131px;background:#fff"></div>
  <div class="card" style="left:111px;top:223px"><div class="img" role="img" aria-label="Illustration of children reading books in front of a chalkboard" style="background:linear-gradient(#2f6b4a,#4e8c63)"></div><h3>Educational</h3><p>Perspiciatis unde omnis iste natus error sit voluptatem accusantium doloremque laudantium, totam rem aperiam, eaque ipsa quae.</p><a>Learn More</a></div>
  <div class="card" style="left:359px;top:164px"><div class="img" role="img" aria-label="Photo of fresh vegetables, fruit and nuts on a table" style="background:linear-gradient(#6b4a2c,#8f6b3a)"></div><h3>Nutritional</h3><p>Perspiciatis unde omnis iste natus error sit voluptatem accusantium doloremque laudantium, totam rem aperiam, eaque ipsa quae.</p><a>Learn More</a></div>
  <div class="card" style="left:606px;top:223px"><div class="img" role="img" aria-label="Photo of a child at a dental check-up" style="background:linear-gradient(#cfd6dc,#9ab0c0)"></div><h3>Dental Health</h3><p>Perspiciatis unde omnis iste natus error sit voluptatem accusantium doloremque laudantium, totam rem aperiam, eaque ipsa quae.</p><a>Learn More</a></div>
  <div class="card" style="left:852px;top:164px"><div class="img" role="img" aria-label="Playful illustration with a robot and rocket" style="background:linear-gradient(#f3d6a4,#e9bf80)"></div><h3>Tall Meadow Children</h3><p>Perspiciatis unde omnis iste natus error sit voluptatem accusantium doloremque laudantium, totam rem aperiam, eaque ipsa quae.</p><a>Learn More</a></div>
  <div class="btn red" style="left:523px;top:674px;width:154px;height:46px;border:2px solid #fff">View More <span class="arr"><svg width="10" height="10" viewBox="0 0 10 10"><path d="M3 1l4 4-4 4" stroke="#e31b2f" stroke-width="2" fill="none"/></svg></span></div>
</section>

<section class="focus">
  <h2 class="section-title" style="top:2194px">We <b>Focus</b></h2>
  <div class="rule" style="left:581px;top:2252px;background:var(--blue)"></div>
  <svg class="abs" style="left:400px;top:2271px" width="400" height="400" viewBox="0 0 400 400">
    <circle cx="200" cy="200" r="188" fill="none" stroke="#999" stroke-width="2" stroke-dasharray="10 8"/>
    <circle cx="200" cy="200" r="150" fill="#fff"/>
    <circle cx="200" cy="200" r="137" fill="var(--red)"/>
    <circle cx="200" cy="200" r="82" fill="none" stroke="#fff" stroke-width="3"/>
    <text x="200" y="208" text-anchor="middle" fill="#fff" font-family="Poppins,sans-serif" font-size="26" font-weight="700">HAFOG, Inc.</text>
  </svg>
  <div class="focus-icon" style="left:400px;top:2333px"><svg width="44" height="44" viewBox="0 0 44 44" fill="none" stroke="#333" stroke-width="1.6"><circle cx="22" cy="12" r="5"/><circle cx="10" cy="20" r="4"/><circle cx="34" cy="20" r="4"/><path d="M12 36c0-7 4-12 10-12s10 5 10 12M3 36c0-6 3-9 7-9M41 36c0-6-3-9-7-9"/></svg></div>
  <div class="focus-icon" style="left:721px;top:2333px"><svg width="44" height="44" viewBox="0 0 44 44" fill="none" stroke="#333" stroke-width="1.6"><circle cx="15" cy="15" r="6"/><circle cx="30" cy="18" r="5"/><path d="M4 38c0-8 5-13 11-13s11 5 11 13M22 38c0-6 3-11 8-11s8 5 8 11"/></svg></div>
  <div class="focus-icon" style="left:400px;top:2550px"><svg width="44" height="44" viewBox="0 0 44 44" fill="none" stroke="#333" stroke-width="1.6"><circle cx="22" cy="22" r="5"/><circle cx="9" cy="9" r="4"/><circle cx="35" cy="9" r="4"/><circle cx="9" cy="35" r="4"/><circle cx="35" cy="35" r="4"/><path d="M12 12l6 6M32 12l-6 6M12 32l6-6M32 32l-6-6"/></svg></div>
  <div class="focus-icon" style="left:721px;top:2550px"><svg width="44" height="44" viewBox="0 0 44 44" fill="none" stroke="#333" stroke-width="1.6"><circle cx="14" cy="12" r="5"/><circle cx="30" cy="12" r="5"/><circle cx="22" cy="26" r="4"/><path d="M4 38c0-9 4-16 10-16M40 38c0-9-4-16-10-16M15 40c0-5 3-8 7-8s7 3 7 8"/></svg></div>
  <div class="focus-label" style="left:278px;top:2345px;text-align:right;width:100px">Staff<br>Growth</div>
  <div class="focus-label" style="left:813px;top:2345px">Child<br>Development</div>
  <div class="focus-label" style="left:238px;top:2567px;text-align:right;width:140px">Community<br>Partnerships</div>
  <div class="focus-label" style="left:813px;top:2567px">Family<br>Wellness</div>
</section>

<section class="testimonials">
  <div class="testi-bg"></div>
  <h2 class="section-title" style="top:2822px;font-weight:700">Testimonials</h2>
  <div class="rule" style="left:581px;top:2882px;background:var(--blue)"></div>
  <div class="tcard" style="left:111px"><div class="q">99</div><div class="av" role="img" aria-label="Reviewer portrait"></div><h4>MARISOL VANTERO</h4><p>Nam libero tempore, cum soluta nobis est eligendi optio cumque nihil impedit quo minus id quod maxime placeat facere possimus, omnis dit quo minus id qu dit quo minus id qu voluptas assumenda est, omnis dolor repellendus.</p><div class="stars"><svg width="74" height="14" viewBox="0 0 74 14"><g fill="#f5c518" stroke="#333" stroke-width=".6"><path id="st" d="M7 1l1.8 4 4.2.4-3.2 2.8 1 4.1L7 10.1 3.2 12.3l1-4.1L1 5.4l4.2-.4z"/><use href="#st" x="15"/><use href="#st" x="30"/><use href="#st" x="45"/><use href="#st" x="60"/></g></svg></div></div>
  <div class="tcard" style="left:449px"><div class="q">99</div><div class="av" role="img" aria-label="Reviewer portrait"></div><h4>MARISOL VANTERO</h4><p>Nam libero tempore, cum soluta nobis est eligendi optio cumque nihil impedit quo minus id quod maxime placeat facere possimus, omnis dit quo minus id qu dit quo minus id qu voluptas assumenda est, omnis dolor repellendus.</p><div class="stars"><svg width="74" height="14" viewBox="0 0 74 14"><g fill="#f5c518" stroke="#333" stroke-width=".6"><use href="#st"/><use href="#st" x="15"/><use href="#st" x="30"/><use href="#st" x="45"/><use href="#st" x="60"/></g></svg></div></div>
  <div class="tcard" style="left:786px"><div class="q">99</div><div class="av" role="img" aria-label="Reviewer portrait"></div><h4>MARISOL VANTERO</h4><p>Nam libero tempore, cum soluta nobis est eligendi optio cumque nihil impedit quo minus id quod maxime placeat facere possimus, omnis dit quo minus id qu dit quo minus id qu voluptas assumenda est, omnis dolor repellendus.</p><div class="stars"><svg width="74" height="14" viewBox="0 0 74 14"><g fill="#f5c518" stroke="#333" stroke-width=".6"><use href="#st"/><use href="#st" x="15"/><use href="#st" x="30"/><use href="#st" x="45"/><use href="#st" x="60"/></g></svg></div></div>
  <div class="dots" style="left:561px;top:3317px"><i></i><i class="on"></i><i></i><i></i></div>
</section>

<section class="contact">
  <h2>Contact <b>Us</b></h2>
  <div class="rule" style="left:146px;top:3567px"></div>
  <p class="abs" style="left:146px;top:3584px;width:460px;font-size:15px;line-height:26px;color:#444">Perspiciatis unde omnis iste natus error ssadsdit voluptatem accusantium doloremque laudantium, totam rem aperiam, eaque ipsa quaasde.</p>
  <div class="info" style="top:3680px"><div class="ic"><svg width="16" height="16" viewBox="0 0 24 24" fill="#fff"><path d="M6.6 10.8a15 15 0 006.6 6.6l2.2-2.2c.3-.3.7-.4 1-.2 1.1.4 2.3.6 3.6.6.6 0 1 .4 1 1V20c0 .6-.4 1-1 1A17 17 0 013 4c0-.6.4-1 1-1h3.5c.6 0 1 .4 1 1 0 1.3.2 2.5.6 3.6.1.3 0 .7-.2 1z"/></svg></div><div><small>Phone Number</small><span>555-010-0188</span></div></div>
  <div class="info" style="top:3740px"><div class="ic"><svg width="16" height="14" viewBox="0 0 16 12" fill="none" stroke="#fff" stroke-width="1.6"><rect x="1" y="1" width="14" height="10"/><path d="M1 1l7 6 7-6"/></svg></div><div><small>E-mail</small><span>info@harboraidoutreach.org</span></div></div>
  <div class="info" style="top:3800px"><div class="ic"><svg width="14" height="18" viewBox="0 0 14 18" fill="#fff"><path d="M7 0a7 7 0 017 7c0 5-7 11-7 11S0 12 0 7a7 7 0 017-7zm0 4a3 3 0 100 6 3 3 0 000-6z"/></svg></div><div><small>Adresss</small><span>418 Linden Crest Road, Brookvale, TX 75012</span></div></div>
  <div class="field" style="top:3504px;height:40px">Full Name</div>
  <div class="field" style="top:3564px;height:40px">E-mail</div>
  <div class="field" style="top:3624px;height:40px">Phone</div>
  <div class="field" style="top:3684px;height:124px">Enter Your Message</div>
  <div class="btn blue" style="left:627px;top:3827px;width:154px;height:50px;justify-content:space-between;padding:0 16px">Submit <span class="arr"><svg width="10" height="10" viewBox="0 0 10 10"><path d="M3 1l4 4-4 4" stroke="#1565b8" stroke-width="2" fill="none"/></svg></span></div>
</section>

<div class="cta" style="left:113px;background:linear-gradient(135deg,#e31b2f,#c9121f)"><h3>Interested to work with us?</h3><div class="btn dark" style="left:164px;top:130px;width:155px;height:48px;font-size:15px">Job Listings <span class="arr" style="background:var(--blue)"><svg width="10" height="10" viewBox="0 0 10 10"><path d="M3 1l4 4-4 4" stroke="#fff" stroke-width="2" fill="none"/></svg></span></div></div>
<div class="cta" style="left:607px;background:linear-gradient(135deg,#1a6cc0,#0f57a6)"><h3>Need Our Serivces&gt;</h3><div class="btn dark" style="left:150px;top:130px;width:182px;height:48px;font-size:15px">Pre-Apply Now <span class="arr" style="background:var(--red)"><svg width="10" height="10" viewBox="0 0 10 10"><path d="M3 1l4 4-4 4" stroke="#fff" stroke-width="2" fill="none"/></svg></span></div></div>

<footer class="footer">
  <div class="abs" style="left:270px;top:108px;display:flex;align-items:center;gap:12px;font-size:26px;font-weight:700"><span style="width:26px;height:26px;border-radius:50%;background:#fff;display:block"></span>HAFOG, Inc.</div>
  <div class="abs" style="left:322px;top:230px;display:flex;gap:18px" aria-label="Social links"><i style="width:14px;height:14px;border-radius:50%;border:2px solid #fff;display:block"></i><i style="width:14px;height:14px;border-radius:50%;border:2px solid #fff;display:block"></i><i style="width:14px;height:14px;border-radius:50%;border:2px solid #fff;display:block"></i></div>
  <div class="fcol" style="left:580px"><h5>Quick Links</h5><div class="rl"></div>Home<br>About<br>Services<br>Blog<br>Testimonials<br>Contact Us</div>
  <div class="fcol" style="left:735px"><h5>Links</h5><div class="rl"></div>Copyright<br>Legal<br>Privacy<br>Accessibility<br>Sitemap</div>
  <div class="fcol" style="left:874px"><h5>Support</h5><div class="rl"></div>Team<br>About Us<br>Careers<br>Our Values</div>
  <div class="abs" style="left:1114px;top:280px;width:40px;height:40px;border-radius:4px;background:var(--blue);display:flex;align-items:center;justify-content:center"><svg width="12" height="12" viewBox="0 0 10 10"><path d="M1 7l4-4 4 4" stroke="#fff" stroke-width="2" fill="none"/></svg></div>
  <div class="abs" style="left:113px;top:314px;width:976px;height:2px;background:var(--red)"></div>
  <div class="abs" style="left:0;width:1200px;top:350px;text-align:center;font-size:14px">©2024. All rights reserved.</div>
  <div class="abs" style="left:1122px;top:352px;font-size:11px">C44</div>
</footer>

</body>
</html>
```